Business card for auto dealership

Looking for a clean modern design.
Would like attached logo incorporated

Industry/Entity Type

Car dealership

Contact Information for Business Card

Name, website, phone, cell, fax, email

```html
<!DOCTYPE html>
<html lang="en">
<head>
<meta charset="utf-8">
<title>Halvorsen Truck &amp; Auto Sales – Business Card</title>
<link href="https://fonts.googleapis.com/css2?family=Montserrat:wght@400;600;700&display=swap" rel="stylesheet">
<style>
  :root {
    --stage: #4a4a4a;
    --paper: #ffffff;
    --ink: #111111;
    --muted: #333333;
    --card-black: #151515;
    --silver: #9a9a9a;
  }
  * { box-sizing: border-box; margin: 0; padding: 0; }
  html, body { width: 1200px; height: 801px; overflow: hidden; }
  body {
    background: var(--stage);
    font-family: "Montserrat", Arial, sans-serif;
    position: relative;
  }
  .card {
    position: absolute;
    top: 257px;
    width: 500px;
    height: 286px;
    overflow: hidden;
  }
  .card-front { left: 70px; background: var(--paper); color: var(--ink); }
  .card-back { left: 630px; background: var(--card-black); display: flex; align-items: center; justify-content: center; }

  .brand {
    position: absolute;
    right: 40px;
    top: 38px;
    text-align: right;
    font-weight: 700;
    line-height: 1;
  }
  .brand-name { font-size: 34px; letter-spacing: -0.5px; display: block; }
  .brand-tag { font-size: 10px; letter-spacing: 1.5px; display: block; margin-top: 4px; }

  .divider-top {
    position: absolute;
    left: 215px; right: 30px; top: 112px;
    border-top: 1px solid var(--ink);
  }
  .website {
    position: absolute;
    right: 40px; top: 196px;
    font-size: 11px;
    color: var(--muted);
  }
  .edge-tab {
    position: absolute;
    right: 0; top: 178px;
    width: 18px; height: 62px;
    background: var(--ink);
  }

  .person-name {
    position: absolute;
    left: 30px; top: 166px;
    font-size: 15px; font-weight: 700; letter-spacing: 0.5px;
  }
  .divider-name {
    position: absolute;
    left: 30px; width: 210px; top: 190px;
    border-top: 1px solid var(--ink);
  }
  .contacts {
    position: absolute;
    left: 30px; top: 198px;
    list-style: none;
    font-size: 10.5px;
    color: var(--muted);
  }
  .contacts li { display: flex; align-items: center; gap: 7px; height: 16px; }
  .contacts svg { width: 9px; height: 9px; fill: var(--ink); flex: none; }

  .back-brand { text-align: center; color: var(--silver); font-weight: 700; line-height: 1; }
  .back-brand .brand-name { font-size: 56px; }
  .back-brand .brand-tag { font-size: 14px; letter-spacing: 2px; margin-top: 6px; }
</style>
</head>
<body>
  <section class="card card-front" aria-label="Business card front">
    <div class="brand">
      <span class="brand-name">Halvorsen</span>
      <span class="brand-tag">TRUCK &amp; AUTO SALES</span>
    </div>
    <div class="divider-top"></div>
    <p class="website">Halvorsenauto.com</p>
    <div class="edge-tab"></div>

    <h1 class="person-name">DANA HALVORSEN</h1>
    <div class="divider-name"></div>
    <ul class="contacts">
      <li><svg viewBox="0 0 10 10" aria-hidden="true"><path d="M2 0.5 L4 2.5 L3 4 Q4.5 6 6 7 L7.5 6 L9.5 8 L8 9.5 Q3 9 0.5 2 Z"/></svg>555-310-4827</li>
      <li><svg viewBox="0 0 10 10" aria-hidden="true"><path d="M2.5 0 H7.5 V10 H2.5 Z M3.5 1 V8 H6.5 V1 Z"/></svg>555-642-9015</li>
      <li><svg viewBox="0 0 10 10" aria-hidden="true"><path d="M2.5 0 H7.5 V3 H2.5 Z M0.5 3.5 H9.5 V7.5 H7.5 V10 H2.5 V7.5 H0.5 Z"/></svg>555-207-3368</li>
      <li><svg viewBox="0 0 10 10" aria-hidden="true"><path d="M0.5 2 H9.5 V8.5 H0.5 Z M0.5 2 L5 5.5 L9.5 2" /></svg>dana@halvorsenauto.com</li>
    </ul>
  </section>

  <section class="card card-back" aria-label="Business card back">
    <div class="back-brand">
      <span class="brand-name">Halvorsen</span>
      <span class="brand-tag">TRUCK &amp; AUTO SALES</span>
    </div>
  </section>
</body>
</html>
```